Landing page for a cyber security service provider called 'Quill Vantor'

The client is a new cyber security company in need of a website landing page at quillvantor.com.

Their visual identity is modern, playful, clean and uncluttered and represents innovation, connectivity and approachability.

The company logo is provided in black (attached) but the client is open to changing the colour to align with the new website design.

The landing page needs to contain:
- A call to action with a 'Get Started' button
-Links to blank 'How it works', 'Products', 'Pricing', 'About Us' and 'Contact Us' pages (that we'll fill out later)

Target Market(s)

Medium to large businesses who probably don't understand cyber / cyber security but need their business to be protected.

Industry/Entity Type

Cyber Security

Coding

Coded - Design and coding required

Number of Pages Required

1 page

Font styles to use
Sans Serif
Other font styles liked:
• Helvetica

Requirements
Nice to have
• Hero banner at the top of the landing page.
Should not have
• Should not look like a traditional cyber / cyber security design (eg no dark blue/ black, red/black colour combinations). Please no military styles (eg no shields, cannons, swords, guns)

```html
<!DOCTYPE html>
<html lang="en">
<head>
<meta charset="utf-8">
<title>Quill Vantor — Next-Gen Cybersecurity Made Simple</title>
<link rel="stylesheet" href="https://fonts.googleapis.com/css2?family=Poppins:ital,wght@0,400;0,500;0,600;1,400&family=Lato:wght@400&display=swap">
<style>
:root{
  --blue:#1a86f0;
  --blue-dark:#0f6fd6;
  --ink:#2f2f33;
  --text:#4a4a50;
  --muted:#8a8a90;
  --yellow:#f7c65a;
  --coral:#f0776c;
  --orange:#f6a01a;
  --line:#e4e6ea;
  --bg:#ffffff;
  --soft:#f6f8fc;
}
*{box-sizing:border-box;margin:0;padding:0}
html,body{width:1200px;height:4140px;overflow:hidden}
body{position:relative;background:linear-gradient(180deg,var(--soft) 0,#fff 700px,#fff 2150px,var(--soft) 2300px,#fff 2900px,#fff 3700px,var(--soft) 4140px);font-family:"Poppins",Helvetica,Arial,sans-serif;color:var(--text)}
.abs{position:absolute}
a{color:inherit;text-decoration:none}
.btn{position:absolute;display:flex;align-items:center;justify-content:center;background:var(--blue);color:#fff;font-weight:600;font-size:15px;letter-spacing:.2px;border-radius:5px;box-shadow:0 6px 14px rgba(26,134,240,.3);text-transform:uppercase}
.brand{position:absolute;font-weight:600;font-size:30px;color:var(--ink);letter-spacing:-.5px;display:flex;align-items:center;gap:12px}
.brand .dot{width:22px;height:22px;border-radius:50%;background:var(--blue)}
.nav{position:absolute;top:36px;left:654px;display:flex;gap:28px;font-size:15px;color:#555}
.center{left:0;width:1200px;text-align:center}
h1{font-weight:600;font-size:48px;line-height:57px;color:var(--ink)}
h1 span{color:var(--blue)}
h2{font-weight:600;font-size:45px;line-height:57px;color:var(--ink)}
.lead{font-size:17.5px;line-height:30px;color:var(--text)}
.art{position:absolute;border-radius:24px}
.step-num{position:absolute;font-weight:600;font-size:26px;color:var(--ink)}
.step-num i{position:absolute;left:18px;top:2px;width:36px;height:36px;border-radius:50%;z-index:-1}
.step-title{position:absolute;font-weight:500;font-size:20px;color:var(--ink)}
.step-text{position:absolute;width:485px;font-size:14.5px;line-height:27.5px;color:#3e3e44}
.toggle-label{position:absolute;top:2496px;font-size:14.5px;font-weight:500;text-transform:uppercase}
.toggle{position:absolute;left:579px;top:2492px;width:64px;height:32px;border-radius:16px;background:#eef1f6}
.toggle b{position:absolute;left:5px;top:5px;width:22px;height:22px;border-radius:50%;background:var(--blue)}
.card{position:absolute;top:2592px;width:252px;height:444px;background:#fff;border-radius:8px;box-shadow:0 8px 24px rgba(30,50,90,.09);text-align:center;overflow:hidden}
.card h3{margin-top:40px;font-weight:400;font-size:21px;color:var(--ink)}
.card .price{margin-top:10px;font-size:44px;font-weight:600;color:var(--ink);line-height:52px}
.card .price small{font-size:13px;font-weight:400;color:#555;margin-right:6px;vertical-align:middle}
.card .sub{margin-top:10px;font-size:13px;color:#555}
.card .rule{width:46px;height:3px;background:var(--blue);margin:20px auto 24px}
.card ul{list-style:none;font-family:"Lato",Helvetica,sans-serif;font-size:13px;line-height:25.5px;color:#444}
.card .btn{left:41px;top:352px;width:170px;height:42px;font-size:14px;box-shadow:none}
.card .band{position:absolute;left:0;bottom:0;width:100%;height:8px}
.testimonial{position:absolute;left:111px;top:3337px;width:978px;height:351px;background:#fff;box-shadow:0 8px 26px rgba(30,50,90,.08);border-bottom:9px solid var(--yellow);border-radius:4px}
.quote{position:absolute;left:120px;top:128px;width:738px;text-align:center;font-style:italic;font-size:16px;line-height:30px;color:#555}
.f-head{position:absolute;top:3858px;font-size:15.5px;font-weight:600;color:var(--blue);letter-spacing:.3px}
.f-list{position:absolute;top:3893px;font-size:15.5px;line-height:25.5px;color:#333;list-style:none}
.social{position:absolute;top:4076px;width:29px;height:29px;border:1.6px solid #333;border-radius:50%}
</style>
</head>
<body>

<!-- Header -->
<header>
  <div class="brand" style="left:115px;top:80px"><span class="dot"></span>Quill Vantor</div>
  <nav class="nav"><a href="#">How it works</a><a href="#">Pricing</a><a href="#">About Us</a></nav>
  <a class="btn" href="#" style="left:942px;top:25px;width:148px;height:44px;font-size:14px">Get Started</a>
</header>

<!-- Hero -->
<section>
  <h1 class="abs center" style="top:116px"><span>Next-Gen</span> Cybersecurity<br>Made Simple</h1>
  <p class="abs center lead" style="top:242px">Protect Your Business with Proactive Cyber Defence Solutions –<br>No Expertise Required</p>
  <a class="btn" href="#" style="left:527px;top:332px;width:148px;height:43px;font-size:14px">Get Started</a>
  <div class="art" role="img" aria-label="Illustration of a team working at desks and a person relaxing with a laptop in a bright office" style="left:112px;top:372px;width:976px;height:262px;background:linear-gradient(90deg,#fdf1e3 0%,#eef3fb 55%,#bcd2f5 85%,#9ebdf0 100%)"></div>
</section>

<!-- How it works -->
<section>
  <h2 class="abs center" style="top:730px">How It Works</h2>
  <p class="abs center lead" style="top:795px">Lorem ipsum dolor sit amet, consectetur adipiscing elit, sed do eiusmod<br>tempor incididunt ut labore et dolore magna aliqua.</p>

  <div class="step-num" style="left:112px;top:948px">01<i style="background:#a9cdf6"></i></div>
  <div class="step-title" style="left:115px;top:1012px">Comprehensive Threat Detection</div>
  <p class="step-text" style="left:113px;top:1049px">Lorem ipsum dolmt, consectetur adipiscing elit, sed do eiusmod tempor incididunt ut labore et dolore magna aliqua. Quis ipsum suspendisse ultrices gravida. Risus commodo viverra maecenas accumsan lacus vel facilisis sed do eiusmod tempor incididunt.</p>
  <a class="btn" href="#" style="left:113px;top:1182px;width:149px;height:44px;font-size:14px">View More</a>
  <div class="art" role="img" aria-label="Illustration of a person with a laptop beside a padlock and password screens" style="left:720px;top:930px;width:310px;height:340px;background:linear-gradient(160deg,#eaf1fd,#fdf3df)"></div>

  <div class="art" role="img" aria-label="Illustration of two colleagues at a desk with monitors showing system dashboards" style="left:168px;top:1375px;width:332px;height:265px;background:linear-gradient(160deg,#dce9fb,#fde9c8)"></div>
  <div class="step-num" style="left:620px;top:1367px">02<i style="background:#fbe4ae"></i></div>
  <div class="step-title" style="left:621px;top:1435px">Simplified Security Management</div>
  <p class="step-text" style="left:621px;top:1470px">Lorem ipsum dolmt, consectetur adipiscing elit, sed do eiusmod tempor incididunt ut labore et dolore magna aliqua. Quis ipsum suspendisse ultrices gravida. Risus commodo viverra maecenas accumsan lacus vel facilisis sed do eiusmod tempor incididunt.</p>
  <a class="btn" href="#" style="left:621px;top:1602px;width:149px;height:44px;font-size:14px">View More</a>

  <div class="step-num" style="left:112px;top:1791px">03<i style="background:#f8c3bf"></i></div>
  <div class="step-title" style="left:113px;top:1860px">Automated Incident Response</div>
  <p class="step-text" style="left:113px;top:1893px">Lorem ipsum dolmt, consectetur adipiscing elit, sed do eiusmod tempor incididunt ut labore et dolore magna aliqua. Quis ipsum suspendisse ultrices gravida. Risus commodo viverra maecenas accumsan lacus vel facilisis sed do eiusmod tempor incididunt.</p>
  <a class="btn" href="#" style="left:113px;top:2028px;width:149px;height:44px;font-size:14px">View More</a>
  <div class="art" role="img" aria-label="Illustration of a laptop with a padlock surrounded by cloud, key, folder and document icons" style="left:650px;top:1793px;width:410px;height:250px;background:linear-gradient(160deg,#e4eefc,#eef3f8)"></div>
</section>

<!-- Pricing -->
<section>
  <h2 class="abs center" style="top:2264px">Choose the Right Plan<br>for Your Needs</h2>
  <p class="abs center lead" style="top:2393px">Lorem ipsum dolor sit amet, consectetur adipiscing elit, sed do eiusmod<br>tempor incididunt ut labore et dolore magna aliqua.</p>
  <div class="toggle-label" style="left:455px;color:var(--blue)">Pay Monthly</div>
  <div class="toggle"><b></b></div>
  <div class="toggle-label" style="left:658px;color:var(--muted)">Pay Yearly</div>

  <div class="card" style="left:174px">
    <h3>Basic Plan</h3>
    <div class="price"><small>from</small>$95</div>
    <div class="sub">Lorem Ipsum Set Amit</div>
    <div class="rule"></div>
    <ul><li>Sed ut perspiciatis</li><li>Unde omnis iste natus error sit</li><li>Voluptatem accusantium dolorem</li><li>Que laudantium, totam rem</li><li>Aperiam, eaque ipsa quae ab illo</li></ul>
    <a class="btn" href="#">Get Started</a>
    <div class="band" style="background:var(--blue)"></div>
  </div>
  <div class="card" style="left:474px">
    <h3>Basic Plan</h3>
    <div class="price"><small>from</small>$105</div>
    <div class="sub">Lorem Ipsum Set Amit</div>
    <div class="rule"></div>
    <ul><li>Sed ut perspiciatis</li><li>Unde omnis iste natus error sit</li><li>Voluptatem accusantium dolorem</li><li>Que laudantium, totam rem</li><li>Aperiam, eaque ipsa quae ab illo</li></ul>
    <a class="btn" href="#">Get Started</a>
    <div class="band" style="background:var(--yellow)"></div>
  </div>
  <div class="card" style="left:775px">
    <h3>Basic Plan</h3>
    <div class="price"><small>from</small>$125</div>
    <div class="sub">Lorem Ipsum Set Amit</div>
    <div class="rule"></div>
    <ul><li>Sed ut perspiciatis</li><li>Unde omnis iste natus error sit</li><li>Voluptatem accusantium dolorem</li><li>Que laudantium, totam rem</li><li>Aperiam, eaque ipsa quae ab illo</li></ul>
    <a class="btn" href="#">Get Started</a>
    <div class="band" style="background:var(--coral)"></div>
  </div>
</section>

<!-- Testimonials -->
<section>
  <h2 class="abs center" style="top:3180px">Client Testimonials</h2>
  <div class="testimonial">
    <div role="img" aria-label="Client portrait" style="position:absolute;left:437px;top:-42px;width:104px;height:104px;border-radius:50%;background:linear-gradient(160deg,#f9d3c4,#bcd6f6);border:4px solid #cfe1f8"></div>
    <div style="position:absolute;left:0;width:100%;top:90px;text-align:center;color:var(--orange);font-size:17px;letter-spacing:2px">★★★★★</div>
    <svg style="position:absolute;left:33px;top:172px" width="30" height="20" viewBox="0 0 30 20"><path d="M28 10H3M11 2 3 10l8 8" fill="none" stroke="var(--blue)" stroke-width="2.4" stroke-linecap="round" stroke-linejoin="round"/></svg>
    <svg style="position:absolute;right:33px;top:172px" width="30" height="20" viewBox="0 0 30 20"><path d="M2 10h25M19 2l8 8-8 8" fill="none" stroke="var(--blue)" stroke-width="2.4" stroke-linecap="round" stroke-linejoin="round"/></svg>
    <p class="quote">Lorem ipsum dolor sit ametctetur adipiscinelit, sed do eiusmod tempor incididunt ut labore et dolore magna aliqua. Ut enim ad minim veniam, quis nostrud exercitation ullamco laborisnisi ut aliquip ex ea commodo cquat. Duis aute irure dolor in rehenderit in voluptateelit esse cillum dolore eu fugiat nulla pariatur.</p>
    <div style="position:absolute;left:0;width:100%;top:278px;text-align:center;font-size:15px;color:#444"><strong style="font-weight:500;color:var(--ink)">Mara Elden</strong>, CEO Lorem Ipsum</div>
  </div>
</section>

<!-- Footer -->
<footer>
  <div class="brand" style="left:113px;top:3930px"><span class="dot"></span>Quill Vantor</div>
  <div class="f-head" style="left:373px">QUICK LINKS</div>
  <ul class="f-list" style="left:373px"><li>How it works</li><li>Pricing</li><li>About Us</li></ul>
  <div class="f-head" style="left:605px">QUICK LINKS</div>
  <ul class="f-list" style="left:605px"><li>Contact Us</li><li>Terms &amp; Conditions</li><li>Privacy Policy</li></ul>
  <div class="f-head" style="left:891px">CONTACT US</div>
  <svg class="abs" style="left:891px;top:3896px" width="14" height="18" viewBox="0 0 14 18"><path d="M7 1a6 6 0 0 0-6 6c0 4.5 6 10 6 10s6-5.5 6-10a6 6 0 0 0-6-6z" fill="#222"/><circle cx="7" cy="7" r="2.2" fill="#fff"/></svg>
  <div class="abs" style="left:921px;top:3893px;font-size:15.5px;line-height:25.5px;color:#333">Quill Vantor,<br>Address Comes Here</div>
  <svg class="abs" style="left:891px;top:3952px" width="15" height="15" viewBox="0 0 24 24"><path d="M6.6 10.8a15.1 15.1 0 0 0 6.6 6.6l2.2-2.2a1 1 0 0 1 1-.25 11.4 11.4 0 0 0 3.6.57 1 1 0 0 1 1 1V20a1 1 0 0 1-1 1A17 17 0 0 1 3 4a1 1 0 0 1 1-1h3.5a1 1 0 0 1 1 1c0 1.25.2 2.45.57 3.6a1 1 0 0 1-.25 1z" fill="#222"/></svg>
  <div class="abs" style="left:921px;top:3947px;font-size:15.5px;color:#333">+1 555-010-2040</div>
  <svg class="abs" style="left:891px;top:3986px" width="15" height="12" viewBox="0 0 15 12"><rect width="15" height="12" rx="1.5" fill="#222"/><path d="M1 1.5l6.5 5 6.5-5" fill="none" stroke="#fff" stroke-width="1.3"/></svg>
  <div class="abs" style="left:921px;top:3980px;font-size:15.5px;color:#333">info@quillvantor.com</div>

  <div class="abs" style="left:111px;top:4052px;width:978px;height:1px;background:var(--line)"></div>
  <div class="abs" style="left:111px;top:4081px;font-size:15px;color:#333">2024 Quill Vantor. All Rights Reserved.</div>
  <span class="social" style="left:905px"></span>
  <span class="social" style="left:944px"></span>
  <span class="social" style="left:983px"></span>
  <span class="social" style="left:1022px"></span>
  <span class="social" style="left:1061px"></span>
</footer>

</body>
</html>
```